Professional, Attractive, Simple Website Needed!!

We completed the design for our logo.

We need a website built out around this.

Here are a couple samples of how we want ours formatted.

http://brvtawatt.com

http://www.brightmerlo.com/lp/free-quote?LeadSource=Search%20Engine&ProgramName=webfind&experience=qual&language=en&type=brd&gclid=Xq7LMnvrTPKDWQAbZeRFtoPLmNcGxJbYTUWoKdMvCeWsfRgHyZnXpLoKqwErTyUiOpAsDfGhJkLzXcVb_zxwQ

http://qmorel.co

Project Deadline Extended
Reason: Extending this deadline due to our delay in providing designers with content for each page. This is coming in next 24 hours.

Project Deadline Extended
Reason: Due to scheduling conflicts and extended travel delays related to Puerto Rico, the deadline has been extended. Your patience is greatly appreciated.

Project Deadline Extended
Reason: Travel and scheduling conflicts have made it impossible to give this project the thorough review it deserves, therefore I am extending the deadline. Thank you for your patience!

Target Market(s)

Home Owners who earn 60k + household annually

Industry/Entity Type

It Professional

Coding

Coded - Design and coding required

Number of Pages Required

5+ page

Font styles to use
Serif

Colors
34a7d8
9bcb3c

Requirements
Must have
• Simple
• Lead form Entry (Ability for visitor to enter Name, number and address for a quote)
• Sleek Design
• Professional
• Testimonials
• Use color Scheme of Design Logo Attached
Nice to have
• Video when site starts
• Like this
• https://www.clipvault.com/watch?v=Rk8TpQwZmNe&feature=clipv.lt
Should not have
• Should not include Commercial solar
• Should not include wind power

```html
<!DOCTYPE html>
<html lang="en">
<head>
<meta charset="utf-8">
<title>Terra Lumen Energy</title>
<link href="https://fonts.googleapis.com/css2?family=Roboto:wght@300;400;500;700&display=swap" rel="stylesheet">
<style>
:root{
  --sky-deep:#1f3aa8;
  --sky-mid:#3a63c8;
  --sky-light:#6f8fd4;
  --ink:#000;
  --footer:#2e2e2e;
  --white:#fff;
  --muted:#c4c4c4;
  --accent:#2a74f5;
  --lime:#8ab22b;
  --field:#404040;
  --field-edge:#262626;
  --field-text:#a8a8a8;
  --brand-blue:#34a7d8;
}
*{box-sizing:border-box;margin:0;padding:0}
html,body{width:1200px;height:1086px;overflow:hidden;background:var(--ink)}
body{position:relative;font-family:'Roboto',sans-serif;color:var(--white)}
.hero-photo{position:absolute;left:0;top:0;width:1200px;height:600px;
  background:linear-gradient(180deg,var(--sky-deep) 0%,var(--sky-mid) 45%,var(--sky-light) 75%,#4d6dc0 100%)}
.section-cut{position:absolute;left:0;top:0}
.brand{position:absolute;left:58px;top:70px;display:flex;align-items:center;gap:8px;
  font-size:19px;font-weight:500;color:var(--brand-blue);letter-spacing:.5px}
.brand-dot{width:14px;height:14px;border-radius:50%;background:var(--brand-blue)}
.nav{position:absolute;top:39px;left:0;width:1200px;font-size:12.5px;font-weight:500;letter-spacing:1.2px}
.nav a{position:absolute;color:var(--white);text-decoration:none;white-space:nowrap}
.hero-title{position:absolute;top:152px;left:0;width:1200px;text-align:center;font-size:57px;font-weight:500;letter-spacing:.5px}
.hero-sub{position:absolute;top:232px;left:0;width:1200px;text-align:center;font-size:17px;font-weight:300;letter-spacing:1.6px}
.btn{position:absolute;display:flex;align-items:center;justify-content:center;gap:10px;background:var(--accent);
  color:var(--white);border-radius:20px;font-size:14px;font-weight:500;letter-spacing:1.6px;text-decoration:none}
.btn-start{left:470px;top:286px;width:244px;height:38px}
.play{width:0;height:0;border-left:10px solid var(--white);border-top:6px solid transparent;border-bottom:6px solid transparent}
.lead-form{position:absolute;left:420px;top:432px;width:345px;height:517px;background:var(--lime)}
.field{position:absolute;left:27px;width:291px;height:54px;background:var(--field);border:1px solid var(--field-edge);
  color:var(--field-text);font-size:12.5px;padding:20px 14px 0}
.field-msg{height:135px;padding-top:9px}
.btn-talk{left:27px;top:434px;width:137px;height:38px}
.info{position:absolute;top:636px;width:360px}
.info h2{font-size:38px;font-weight:700;letter-spacing:-.3px}
.info p{margin-top:41px;font-size:17px;line-height:27px;color:var(--muted);font-weight:400}
.info-about{left:30px}
.info-why{left:810px}
.btn-more{position:absolute;top:270px;left:0;width:147px;height:38px}
.to-top{position:absolute;left:1130px;width:42px;height:31px;background:#333;border-radius:3px 3px 0 0;display:flex;align-items:center;justify-content:center}
.footer{position:absolute;left:0;top:1003px;width:1200px;height:83px;background:var(--footer)}
.copyright{position:absolute;left:58px;top:37px;font-size:12px;color:#e6e6e6}
.social{position:absolute;top:26px;width:34px;height:34px;border-radius:50%;background:var(--white)}
</style>
</head>
<body>
<div class="hero-photo" role="img" aria-label="Photo of a row of wind turbines on a blue sky"></div>
<svg class="section-cut" width="1200" height="1086" viewBox="0 0 1200 1086" aria-hidden="true">
  <polygon points="0,591 420,530 765,530 1200,594 1200,1086 0,1086" fill="#000"/>
</svg>

<div class="brand"><span class="brand-dot"></span>TERRA LUMEN ENERGY</div>

<nav class="nav">
  <a href="#" style="left:625px">HOME</a>
  <a href="#" style="left:706px">ABOUT</a>
  <a href="#" style="left:793px">HOW ITS WORK</a>
  <a href="#" style="left:937px">SERVICES</a>
  <a href="#" style="left:1042px">CONTACT US</a>
</nav>

<h1 class="hero-title">TERRA LUMEN ENERGY</h1>
<p class="hero-sub">EXPERIENCE UNPARALLELED FREEDOM OF ENERGY SAVING</p>
<a class="btn btn-start" href="#"><span class="play"></span>START YOUR SEAVING</a>

<div class="to-top" style="top:562px"><svg width="12" height="8" viewBox="0 0 12 8"><path d="M1 7l5-5 5 5" fill="none" stroke="#ddd" stroke-width="1.6"/></svg></div>

<form class="lead-form">
  <div class="field" style="top:27px">NAME</div>
  <div class="field" style="top:117px">EMAIL</div>
  <div class="field" style="top:207px">PHONE</div>
  <div class="field field-msg" style="top:280px">HOW CAN WE HELP?</div>
  <a class="btn btn-talk" href="#">LET'S TALK</a>
</form>

<section class="info info-about">
  <h2>About Us</h2>
  <p>Lorem ipsum dolor sit amet, consectetur adipiscing elit. Donec elementum ornare massa. Mauris quis bibendum nibh. Nulla eu efficitur sem, eu vulputate urna. Nullam posuere erat id velit cursus ultricies. Phasellus nec mauris sapien.</p>
  <a class="btn btn-more" href="#">READ MORE</a>
</section>

<section class="info info-why">
  <h2>Why Us</h2>
  <p>Lorem ipsum dolor sit amet, consectetur adipiscing elit. Donec elementum ornare massa. Mauris quis bibendum nibh. Nulla eu efficitur sem, eu vulputate urna. Nullam posuere erat id velit cursus ultricies. Phasellus nec mauris sapien.</p>
  <a class="btn btn-more" href="#">READ MORE</a>
</section>

<footer class="footer">
  <p class="copyright">© Copyright 2017 &nbsp;| &nbsp;Terra Lumen Energy &nbsp;| &nbsp;All Rights Reserved</p>
  <span class="social" style="left:1006px"></span>
  <span class="social" style="left:1049px"></span>
  <span class="social" style="left:1092px"></span>
  <div class="to-top" style="top:52px"><svg width="12" height="8" viewBox="0 0 12 8"><path d="M1 7l5-5 5 5" fill="none" stroke="#ddd" stroke-width="1.6"/></svg></div>
</footer>
</body>
</html>
```